Agriculture Business Card

I want to use my existing logo and use my tagline of "Don't Guess...Soil Test" on the card. Looking for a double sided card that will really get peoples attention.
Contact Info:
Brisco Harvest Crop Solutions
Calvin Brisco
2917 K Lane
Otoe, NE 68539
402-815-2493
calvin.r.brisco@furrowpost.net

```html
<!DOCTYPE html>
<html lang="en">
<head>
<meta charset="utf-8">
<title>Brisco Harvest Crop Solutions – Business Card</title>
<link href="https://fonts.googleapis.com/css2?family=Roboto:wght@400;500;700&display=swap" rel="stylesheet">
<style>
  :root {
    --bg: #c9c9c9;
    --card-cream: #e8dad1;
    --card-green: #3db22d;
    --brown: #a4522b;
    --text-gray: #5b5b5b;
    --gold: #f5b21b;
    --white: #ffffff;
  }
  * { margin: 0; padding: 0; box-sizing: border-box; }
  html, body { width: 1200px; height: 800px; overflow: hidden; }
  body {
    background: linear-gradient(180deg, #dcdcdc 0%, var(--bg) 100%);
    font-family: "Roboto", Arial, sans-serif;
    position: relative;
  }
  .card {
    position: absolute;
    top: 245px;
    width: 540px;
    height: 309px;
    box-shadow: 0 10px 24px rgba(0,0,0,0.22);
  }
  .card--contact { left: 40px; background: var(--card-cream); }
  .card--tagline { left: 620px; background: var(--card-green); }

  /* Contact side */
  .brand-block {
    position: absolute;
    left: 36px;
    top: 0;
    width: 170px;
    height: 100%;
    display: flex;
    align-items: center;
    gap: 10px;
  }
  .brand-dot {
    flex: 0 0 22px;
    height: 22px;
    border-radius: 50%;
    background: var(--gold);
  }
  .brand-name {
    color: var(--brown);
    font-weight: 500;
    font-size: 17px;
    line-height: 1.2;
  }
  .divider {
    position: absolute;
    left: 224px;
    top: 92px;
    width: 1.5px;
    height: 126px;
    background: var(--brown);
  }
  .contact {
    position: absolute;
    left: 248px;
    top: 88px;
    color: var(--text-gray);
    font-size: 13px;
    line-height: 1.35;
  }
  .contact__name {
    color: var(--brown);
    font-weight: 700;
    font-size: 19px;
    letter-spacing: 0.3px;
    margin-bottom: 8px;
  }
  .contact__address { margin-bottom: 10px; }
  .contact__line { display: flex; align-items: center; gap: 7px; }
  .contact__line svg { width: 11px; height: 11px; flex: 0 0 11px; }

  /* Tagline side */
  .brand-hero {
    position: absolute;
    left: 0; right: 0;
    top: 100px;
    text-align: center;
    color: var(--white);
    font-weight: 500;
    font-size: 26px;
    line-height: 1.25;
    display: flex;
    justify-content: center;
    align-items: center;
    gap: 14px;
  }
  .brand-hero .brand-dot { flex-basis: 28px; height: 28px; }
  .tagline {
    position: absolute;
    left: 0; right: 0;
    top: 232px;
    text-align: center;
    color: var(--white);
    font-size: 14px;
    letter-spacing: 2.2px;
    font-weight: 400;
  }
  .tagline strong { font-weight: 700; }
</style>
</head>
<body>

<section class="card card--contact">
  <div class="brand-block">
    <span class="brand-dot"></span>
    <span class="brand-name">Brisco Harvest Crop Solutions</span>
  </div>
  <div class="divider"></div>
  <div class="contact">
    <div class="contact__name">CALVIN BRISCO</div>
    <div class="contact__address">2917 K Lane<br>Otoe, NE 68539</div>
    <div class="contact__line">
      <svg viewBox="0 0 24 24" aria-hidden="true"><path fill="#a4522b" d="M6.6 10.8a15 15 0 0 0 6.6 6.6l2.2-2.2c.3-.3.7-.4 1-.2 1.1.4 2.3.6 3.6.6.6 0 1 .4 1 1V20c0 .6-.4 1-1 1A17 17 0 0 1 3 4c0-.6.4-1 1-1h3.5c.6 0 1 .4 1 1 0 1.2.2 2.4.6 3.6.1.3 0 .7-.2 1z"/></svg>
      <span>402-815-2493</span>
    </div>
    <div class="contact__line">
      <svg viewBox="0 0 24 24" aria-hidden="true"><rect x="2" y="5" width="20" height="14" rx="1.5" fill="#a4522b"/><path d="M3 6l9 7 9-7" stroke="#e8dad1" stroke-width="1.8" fill="none"/></svg>
      <span>calvin.r.brisco@furrowpost.net</span>
    </div>
    <div class="contact__line">
      <svg viewBox="0 0 24 24" aria-hidden="true"><circle cx="12" cy="12" r="10" fill="#a4522b"/><path d="M2 12h20M12 2c3 3 3 17 0 20M12 2c-3 3-3 17 0 20" stroke="#e8dad1" stroke-width="1.4" fill="none"/></svg>
      <span>briscoharvest.net</span>
    </div>
  </div>
</section>

<section class="card card--tagline">
  <div class="brand-hero">
    <span class="brand-dot"></span>
    <span>Brisco Harvest<br>Crop Solutions</span>
  </div>
  <p class="tagline">DON’T GUESS...<strong>SOIL TEST</strong></p>
</section>

</body>
</html>
```